Needing a business Card for new fire company.

Dalvo, sales fire equipment and parts. We also do tree clearing for the forest service. My logo will be attached to this. I am also looking for a design that when people see the card it stick with them and they will remember my sales team giving it to them.

```html
<!DOCTYPE html>
<html lang="en">
<head>
<meta charset="UTF-8">
<title>Dalvo Business Card</title>
<link rel="stylesheet" href="https://fonts.googleapis.com/css2?family=Arimo:wght@400;700&display=swap">
<style>
  :root {
    --backdrop: #262626;
    --card-white: #ffffff;
    --fire-red: #c1272d;
    --fire-red-light: #e2555c;
    --fire-red-dark: #8f0f14;
    --ink: #111111;
    --rule: #444444;
  }
  * { margin: 0; padding: 0; box-sizing: border-box; }
  html, body {
    width: 1200px;
    height: 1108px;
    overflow: hidden;
    background: var(--backdrop);
    font-family: "Arimo", Arial, sans-serif;
  }
  .stage {
    position: relative;
    width: 1200px;
    height: 1108px;
    display: flex;
    justify-content: center;
    align-items: center;
    gap: 80px;
  }
  .card {
    position: relative;
    width: 420px;
    height: 735px;
    border-radius: 26px;
    overflow: hidden;
    text-align: center;
  }
  .card-front {
    background: var(--card-white);
    color: var(--ink);
  }
  .card-back {
    background: var(--fire-red);
  }
  .brand-name {
    position: absolute;
    left: 0;
    right: 0;
    top: 150px;
    text-align: center;
    font-weight: 700;
    font-size: 88px;
    letter-spacing: 4px;
    text-indent: 4px;
    line-height: 1;
  }
  .card-front .brand-name { color: var(--ink); }
  .card-back .brand-name { color: var(--card-white); }

  .person {
    position: absolute;
    left: 0;
    right: 0;
    top: 340px;
  }
  .person-name {
    color: var(--fire-red);
    font-weight: 700;
    font-size: 30px;
    letter-spacing: 1px;
    text-transform: uppercase;
  }
  .person-title {
    font-size: 24px;
    margin-top: 4px;
  }
  .icon-row {
    position: absolute;
    left: 36px;
    right: 36px;
    top: 440px;
    display: flex;
    align-items: center;
    gap: 10px;
  }
  .icon-row .rule { flex: 1; height: 1px; background: var(--rule); }
  .icon-badge {
    width: 36px;
    height: 36px;
    border-radius: 7px;
    background: var(--fire-red);
    display: flex;
    align-items: center;
    justify-content: center;
  }
  .contact-list {
    position: absolute;
    left: 0;
    right: 0;
    top: 490px;
    list-style: none;
    font-size: 24px;
    line-height: 1.3;
  }
  .divider {
    position: absolute;
    left: 36px;
    right: 36px;
    top: 600px;
    height: 1px;
    background: var(--rule);
  }
  .address {
    position: absolute;
    left: 0;
    right: 0;
    top: 620px;
    font-size: 24px;
    line-height: 1.3;
    font-style: normal;
  }
  .flame-artwork {
    position: absolute;
    left: 0;
    right: 0;
    bottom: 0;
    height: 360px;
    background: linear-gradient(180deg, var(--fire-red) 0%, var(--fire-red-light) 45%, var(--fire-red-dark) 100%);
    opacity: 0.85;
  }
</style>
</head>
<body>
  <main class="stage">
    <section class="card card-front">
      <div class="brand-name">DALVO</div>
      <div class="person">
        <div class="person-name">Marcus Reed</div>
        <div class="person-title">Manager</div>
      </div>
      <div class="icon-row">
        <span class="rule"></span>
        <span class="icon-badge" aria-label="phone">
          <svg width="22" height="22" viewBox="0 0 24 24" fill="none" stroke="#fff" stroke-width="2" stroke-linecap="round" stroke-linejoin="round"><path d="M5 3h4l2 5-3 2a11 11 0 0 0 6 6l2-3 5 2v4a2 2 0 0 1-2 2A17 17 0 0 1 3 5a2 2 0 0 1 2-2z"/></svg>
        </span>
        <span class="icon-badge" aria-label="email">
          <svg width="22" height="22" viewBox="0 0 24 24" fill="none" stroke="#fff" stroke-width="2" stroke-linejoin="round"><rect x="3" y="5" width="18" height="14" rx="1"/><path d="M3 6l9 7 9-7"/></svg>
        </span>
        <span class="icon-badge" aria-label="website">
          <svg width="22" height="22" viewBox="0 0 24 24" fill="none" stroke="#fff" stroke-width="2"><circle cx="12" cy="12" r="9"/><path d="M3 12h18M12 3c3 3 3 15 0 18M12 3c-3 3-3 15 0 18"/></svg>
        </span>
        <span class="rule"></span>
      </div>
      <ul class="contact-list">
        <li>555-014-2100</li>
        <li>sales@dalvofire.com</li>
        <li>www.dalvofire.com</li>
      </ul>
      <div class="divider"></div>
      <address class="address">Your address, city<br>state, ZIP 0000</address>
    </section>

    <section class="card card-back">
      <div class="brand-name">DALVO</div>
      <div class="flame-artwork" role="img" aria-label="Large embossed flame artwork in light and dark red rising from the bottom of the card"></div>
    </section>
  </main>
</body>
</html>
```